Ferrowave.com website design

I need a basic website for www.ferrowave.com. Ferro Wave has been hosting websites since 2002 via partnership arrangement with Stackhollow.com and Namequarry.com. We do not do any design, only hosting for small companies and nonprofits. We are referring people to PixelGuild and others to get their websites developed. Our website and pricing does not change often, but I need to be able to easily update the pricing and contact page.

Target Market(s)

Small company and non profit organizations

Industry/Entity Type

Utility

Coding

Coded - Design and coding required

Number of Pages Required

5+ page

Colors

Designer to choose colors to be used in the design.

Requirements
Must have
• Wordsmith format for easy content management. The logo attached. Contact us page with the following: Phone and fax are the same number: 888.514.2973. Email address is myferrowave@mailnest.example. Mailing address is 4819 E. Tolliver Bend #317, Searcy, AR 72143.
Nice to have
• Some kind of badge or tag line on the home page that celebrates our 15th year of hosting without a single hosting without any downtime. We are are 15 year partners with Stackhollow.com and Namequarry.com. Website Design tab needs to reference PixelGuild or others for all their website design needs. We provide no design or updating services. We will provide the developers FTP access to our dedicated Linux server. We do not provide email services other than redirects to their proprietary email or gmail, yahoo, etc. Needs a services and pricing tab. We provide domain registration services via our partnership with Namequarry.com. We will want a way for them to submit a suggested domain name for us to verify if available. I might be able to get a link from Namequarry.com to our account for you to include on that tab REGISTER DOMAIN. The tab buttons can be: WHO WE ARE, WHAT WE DO, WHEN YOU NEED US, WHERE TO REACH US. Maybe consider making the WHO, WHAT, WHEN and WHERE a dark blue color the rest of the text different color just so they stand out
Should not have
• A lot of animation that takes a long time to open. Clean and simple website.

```html
<!DOCTYPE html>
<html lang="en">
<head>
<meta charset="utf-8">
<title>Ferro Wave — Website Hosting</title>
<link href="https://fonts.googleapis.com/css2?family=Montserrat:wght@300;400;600;700;800&family=Open+Sans:wght@400;600&display=swap" rel="stylesheet">
<style>
  :root {
    --navy-deep: #0b2a55;
    --navy-band: #0c3561;
    --navy-hero: #123f7a;
    --blue-bright: #1e90ff;
    --white: #ffffff;
    --ink: #333a44;
    --ink-soft: #5f6670;
    --line-soft: rgba(255,255,255,0.18);
    --rule-grey: #9aa0a8;
    --page-bg: #ffffff;
  }
  * { box-sizing: border-box; margin: 0; padding: 0; }
  html, body { width: 1200px; height: 1200px; overflow: hidden; background: var(--page-bg); }
  body { position: relative; font-family: "Open Sans", Arial, sans-serif; color: var(--ink); }

  .hero {
    position: absolute; left: 40px; top: 0; width: 1120px; height: 563px;
    background: radial-gradient(ellipse at 45% 40%, #1d5aa6 0%, var(--navy-hero) 45%, var(--navy-deep) 100%);
    overflow: hidden;
  }
  .topbar { position: absolute; left: 0; top: 0; width: 100%; height: 30px; color: var(--white); font-size: 12px; }
  .topbar .call { position: absolute; left: 116px; top: 8px; }
  .topbar .call span { margin-left: 14px; }
  .topbar .account { position: absolute; left: 787px; top: 8px; }
  .topbar .account .sep { margin: 0 8px; }
  .social { position: absolute; left: 918px; top: 9px; display: flex; gap: 18px; }
  .social i { display: block; width: 12px; height: 12px; border-radius: 50%; background: var(--white); }
  .rule { position: absolute; left: 78px; width: 962px; height: 1px; background: var(--line-soft); }
  .rule.top { top: 30px; }
  .rule.nav { top: 110px; }

  .brand { position: absolute; left: 98px; top: 54px; display: flex; align-items: center; gap: 8px; }
  .brand .mark { width: 26px; height: 26px; background: var(--white); }
  .brand .name { font-family: "Montserrat", sans-serif; font-weight: 700; font-size: 16px; letter-spacing: 1px; color: var(--white); text-transform: uppercase; }

  .main-nav { position: absolute; left: 536px; top: 61px; display: flex; gap: 29px; font-family: "Open Sans", sans-serif; font-size: 12px; font-weight: 600; color: var(--white); }
  .main-nav .active { color: var(--blue-bright); }

  .headline { position: absolute; left: 77px; top: 156px; font-family: "Montserrat", sans-serif; color: var(--white); }
  .headline .lead { font-size: 25px; font-weight: 700; margin-left: 4px; line-height: 38px; }
  .headline .big { font-size: 57px; font-weight: 800; line-height: 68px; letter-spacing: -0.5px; }
  .headline .big.accent { color: var(--blue-bright); }
  .hero-copy { position: absolute; left: 81px; top: 324px; width: 490px; color: var(--white); font-size: 15.5px; line-height: 25px; }
  .btn { display: inline-flex; align-items: center; justify-content: center; background: var(--blue-bright); color: var(--white); font-family: "Montserrat", sans-serif; font-weight: 700; font-size: 12px; text-transform: uppercase; }
  .hero .btn { position: absolute; left: 82px; top: 438px; width: 157px; height: 44px; }

  .servers { position: absolute; left: 655px; top: 225px; width: 385px; height: 300px;
    background: linear-gradient(180deg, #3b4049 0%, #1c1f26 70%, #8d939c 100%); border-radius: 4px; }
  .price-badge { position: absolute; left: 590px; top: 228px; width: 92px; height: 92px; border-radius: 50%; background: var(--blue-bright); color: var(--white); font-family: "Montserrat", sans-serif; font-weight: 700; text-align: center; padding-top: 24px; }
  .price-badge .from { font-size: 15px; line-height: 18px; }
  .price-badge .amount { font-size: 19px; line-height: 26px; }
  .price-badge .amount small { font-size: 10px; }

  .domain-bar { position: absolute; left: 40px; top: 563px; width: 1120px; height: 88px; background: var(--navy-band); }
  .domain-bar .label { position: absolute; left: 113px; top: 37px; font-family: "Montserrat", sans-serif; font-weight: 700; font-size: 16.5px; color: var(--white); }
  .domain-field { position: absolute; left: 348px; top: 28px; width: 480px; height: 43px; border: 1px solid rgba(255,255,255,0.15); display: flex; align-items: center; font-size: 12px; color: rgba(255,255,255,0.7); }
  .domain-field .placeholder { flex: 1; padding-left: 15px; }
  .domain-field .tld { width: 82px; height: 100%; border-left: 1px solid rgba(255,255,255,0.15); display: flex; align-items: center; padding-left: 20px; gap: 12px; }
  .domain-bar .btn { position: absolute; left: 861px; top: 31px; width: 128px; height: 36px; }

  .about { position: absolute; left: 0; top: 651px; width: 1200px; text-align: center; }
  .about h2 { margin-top: 20px; font-family: "Montserrat", sans-serif; font-size: 28px; font-weight: 300; color: var(--ink); letter-spacing: 0.5px; }
  .about h2 strong { color: var(--blue-bright); font-weight: 700; }
  .heading-rule { position: relative; width: 126px; height: 1px; background: var(--rule-grey); margin: 10px auto 0; }
  .heading-rule::after { content: ""; position: absolute; left: 40px; top: -1px; width: 46px; height: 3px; background: var(--blue-bright); }
  .about p { width: 930px; margin: 25px auto 0; font-size: 12px; line-height: 20px; color: var(--ink-soft); }

  .showcase { position: absolute; left: 342px; top: 802px; width: 538px; height: 323px; background: linear-gradient(180deg, #1a1d22 0%, #dfe6f1 20%, #e9eef6 80%, #c7cbd0 100%); border-radius: 8px; }

  .pricing-teaser { position: absolute; left: 0; top: 1164px; width: 1200px; text-align: center; font-family: "Montserrat", sans-serif; font-size: 29px; font-weight: 400; color: var(--ink-soft); }
  .pricing-teaser strong { color: var(--blue-bright); font-weight: 700; }
</style>
</head>
<body>
  <header class="hero">
    <div class="topbar">
      <div class="call">Call Us:<span>888.514.2973</span></div>
      <div class="account">Login<span class="sep">|</span>Register</div>
      <div class="social" aria-label="Social links"><i></i><i></i><i></i><i></i></div>
    </div>
    <div class="rule top"></div>
    <div class="brand"><span class="mark"></span><span class="name">Ferro Wave</span></div>
    <nav class="main-nav">
      <span class="active">HOME</span><span>CONTACT US</span><span>VPS</span><span>DOMAIN</span><span>SSL</span><span>MAIL BOXES</span><span>WINDOWS</span>
    </nav>
    <div class="rule nav"></div>

    <div class="headline">
      <div class="lead">WE CELEBRATES OUR</div>
      <div class="big accent">15TH YEAR</div>
      <div class="big">OF HOSTING</div>
    </div>
    <p class="hero-copy">celebrates our 15th year of hosting without a single hosting without any downtime. We are are 15 year partners with Stackhollow.com and Namequarry.com.</p>
    <a class="btn">Get Started Now!</a>

    <div class="servers" role="img" aria-label="Row of server rack cabinets"></div>
    <div class="price-badge">
      <div class="from">Start at</div>
      <div class="amount">4.99 <small>/mo</small></div>
    </div>
  </header>

  <section class="domain-bar">
    <div class="label">Search Your Domain name</div>
    <div class="domain-field">
      <span class="placeholder">Enter your domain name here...</span>
      <span class="tld">.com
        <svg width="8" height="7" viewBox="0 0 8 7"><path d="M0 0h8L4 7z" fill="#1e90ff"/></svg>
      </span>
    </div>
    <a class="btn">Search Domain</a>
  </section>

  <section class="about">
    <h2><strong>WHO</strong> WE ARE</h2>
    <div class="heading-rule"></div>
    <p>We are are 15 year partners with Stackhollow.com and Namequarry.com. Website Design tab needs to reference PixelGuild or others for all their website design needs. We provide no design or updating services. We will provide the developers FTP access to our dedicated Linux server.</p>
  </section>

  <div class="showcase" role="img" aria-label="Laptop showing a sample client website hosted on the service"></div>

  <div class="pricing-teaser">Starting only <strong>$3.0/month</strong></div>
</body>
</html>
```